Kit com 6 Layouts de Post para Redes Sociais (Facebook, Instagram e etc) + Capa de Facebookpara RZ SEGUROS E CONSORCIOS
Postado por: gestao.rzseguros_2840395726   Estou Offline

```html
<!DOCTYPE html>
<html lang="pt-BR">
<head>
<meta charset="UTF-8">
<title>Post para redes sociais — Seguros e Consórcios</title>
<link rel="stylesheet" href="https://fonts.googleapis.com/css2?family=Poppins:wght@400;500;600;700&display=swap">
<style>
  :root {
    --bg-deep: #24143d;
    --bg-mid: #3b2366;
    --violet: #5b3a8e;
    --magenta: #b460c2;
    --lilac: #c98ed8;
    --white: #ffffff;
    --photo-a: #6d5a8f;
    --photo-b: #a07bb8;
  }
  * { margin: 0; padding: 0; box-sizing: border-box; }
  html, body { width: 1200px; height: 1200px; overflow: hidden; background: var(--bg-deep); }
  .post {
    position: relative;
    width: 1200px;
    height: 1200px;
    overflow: hidden;
    font-family: "Poppins", sans-serif;
    background: linear-gradient(160deg, var(--bg-mid) 0%, var(--bg-deep) 75%);
  }
  .post__art { position: absolute; inset: 0; width: 1200px; height: 1200px; }
  .headline {
    position: absolute;
    left: 88px;
    top: 352px;
    font-weight: 600;
    font-size: 80px;
    line-height: 84px;
    letter-spacing: -1px;
  }
  .headline__accent { color: var(--lilac); display: block; }
  .headline__main { color: var(--white); display: block; }
  .brand {
    position: absolute;
    left: 90px;
    top: 1068px;
    color: var(--white);
    font-size: 44px;
    font-weight: 400;
    letter-spacing: 0.5px;
  }
  .contact {
    position: absolute;
    left: 876px;
    top: 1024px;
    color: var(--white);
  }
  .contact__label {
    color: var(--lilac);
    font-size: 16px;
    font-weight: 500;
    letter-spacing: 1px;
    margin-left: 80px;
  }
  .contact__row { display: flex; align-items: center; gap: 10px; }
  .contact__icon {
    width: 30px; height: 30px; border-radius: 50%;
    background: var(--lilac);
    display: flex; align-items: center; justify-content: center;
  }
  .contact__phone { font-size: 40px; font-weight: 700; line-height: 50px; letter-spacing: 0.5px; }
  .contact__phone small { font-size: 20px; font-weight: 600; margin-right: 6px; }
  .contact__handle { font-size: 17px; font-weight: 500; margin-top: 2px; padding-left: 52px; }
  .contact__dot { width: 20px; height: 20px; border-radius: 50%; background: var(--lilac); }
</style>
</head>
<body>
<main class="post">
  <svg class="post__art" viewBox="0 0 1200 1200" xmlns="http://www.w3.org/2000/svg">
    <defs>
      <linearGradient id="photoFill" x1="0" y1="0" x2="1" y2="1">
        <stop offset="0" stop-color="var(--photo-b)"/>
        <stop offset="0.55" stop-color="var(--photo-a)"/>
        <stop offset="1" stop-color="var(--bg-mid)"/>
      </linearGradient>
    </defs>
    <polygon class="photo-area" role="img" aria-label="Foto de dois profissionais sorridentes apertando as mãos em um escritório"
      points="790,40 1300,550 800,1060 300,560" fill="url(#photoFill)"/>
    <polygon class="band band--magenta" points="640,40 900,40 1200,340 1200,620 700,120" fill="var(--magenta)" opacity="0.55"/>
    <polygon class="band band--violet" points="300,560 560,300 620,360 420,560 640,780 580,840" fill="var(--violet)" opacity="0.7"/>
    <polygon class="band band--lower" points="520,1200 900,820 1200,820 1200,1200" fill="var(--violet)" opacity="0.55"/>
    <polyline class="chevron-line" points="470,300 720,560 470,820" fill="none" stroke="var(--bg-deep)" stroke-width="18" opacity="0.8"/>
    <polygon class="chevron chevron--accent" points="696,84 776,84 856,162 776,240 696,240 776,162" fill="var(--magenta)"/>
    <polygon class="chevron chevron--white" points="822,604 920,604 1056,770 920,936 822,936 958,770" fill="var(--white)"/>
  </svg>

  <h1 class="headline">
    <span class="headline__accent">Seu<br>Texto Aqui</span>
    <span class="headline__main">Seu texto<br>aqui.</span>
  </h1>

  <div class="brand">SUA LOGO</div>

  <div class="contact">
    <div class="contact__label">LIGUE AGORA</div>
    <div class="contact__row">
      <span class="contact__icon">
        <svg width="16" height="16" viewBox="0 0 24 24"><path d="M6.6 10.8a15 15 0 0 0 6.6 6.6l2.2-2.2a1 1 0 0 1 1-.25 11.4 11.4 0 0 0 3.6.57 1 1 0 0 1 1 1V20a1 1 0 0 1-1 1A17 17 0 0 1 3 4a1 1 0 0 1 1-1h3.5a1 1 0 0 1 1 1c0 1.25.2 2.45.57 3.6a1 1 0 0 1-.25 1z" fill="var(--bg-deep)"/></svg>
      </span>
      <span class="contact__phone"><small>xx.</small>0000.0000</span>
    </div>
    <div class="contact__row contact__handle">
      <span class="contact__dot"></span>
      <span>@SEUPERFIL</span>
    </div>
  </div>
</main>
</body>
</html>
```